Music Festival in Colorado Needs Awesome Flier Design

We need an eye-catching & captivating flier design for an annual music festival in Denver, CO (USA). The festival features the best Colorado musicians within the genres of jam - funk - bluegrass - electronic - reggae - rock.

The design should look clean and professional while still being creative and unique. The past three years' flier designs are attached, as well as the logo and some other designs that match the aesthetic of what we're looking for.

This festival has a big element of Colorado pride so any

Target Market(s)

Hippies - live music enthusiasts - partiers. Ages 21 - 40.

Industry/Entity Type

Entertainment

Colors
0355a3
ec1f27
ffffff
fbed22

Requirements
Must have
• Attached design text.
Nice to have
• - Quality texture and psychedelic elements.
• - Colorado pride elements; color scheme (red, white, blue & yellow), flag, ect.
• - Nature elements are awesome but this is also a downtown festival so keep that in mind.
Should not have
• Cheesy artwork.

```html
<!DOCTYPE html>
<html lang="en">
<head>
<meta charset="utf-8">
<title>Pass the Echo — 6th Annual High Plains Sound Gathering</title>
<link rel="stylesheet" href="https://fonts.googleapis.com/css2?family=Oswald:wght@500;700&family=Playfair+Display:wght@700&family=Arimo:wght@700&display=swap">
<style>
  :root {
    --paper: #c9bea6;
    --sky-top: #d7dcc6;
    --sky-mid: #a9cbc6;
    --ridge: #3f8c97;
    --deep: #123845;
    --night: #0c2230;
    --ink: #1e3940;
    --ribbon: #b3a68a;
    --ribbon-dark: #8c8068;
    --cream: #f4efe2;
    --frame: #8a8270;
    --info: #cfc2a2;
    --white: #ffffff;
  }
  * { margin: 0; padding: 0; box-sizing: border-box; }
  html, body { width: 995px; height: 1200px; overflow: hidden; background: #e6e6e6; }
  .poster { position: relative; width: 995px; height: 1200px; background: var(--paper); overflow: hidden; }
  .poster-art {
    position: absolute; inset: 12px;
    background: linear-gradient(180deg, var(--sky-top) 0%, var(--sky-mid) 30%, var(--ridge) 52%, var(--deep) 75%, var(--night) 100%);
  }
  .poster-frame { position: absolute; inset: 0; }
  .ribbon { position: absolute; left: 0; top: 0; }
  .edition {
    position: absolute; top: 98px; left: 0; width: 995px; text-align: center;
    font: 700 42px "Playfair Display", serif; color: var(--cream);
    font-variant-numeric: lining-nums;
    transform: rotate(2deg);
  }
  .festival-name {
    position: absolute; top: 172px; left: 0; width: 995px; text-align: center;
    font-family: "Oswald", sans-serif; font-weight: 700; color: var(--ink); text-transform: uppercase;
    line-height: 1;
  }
  .festival-name .lead { display: block; font-size: 50px; letter-spacing: 1px; }
  .festival-name .main { display: block; font-size: 200px; letter-spacing: -4px; margin-top: -6px; }
  .dates {
    position: absolute; top: 452px; left: 0; width: 995px; text-align: center;
    font: 700 56px "Playfair Display", serif; color: var(--cream);
    font-variant-numeric: lining-nums;
    transform: rotate(4deg);
  }
  .lineup {
    position: absolute; top: 622px; left: 0; width: 995px; text-align: center; list-style: none;
    font: 500 41px/56px "Oswald", sans-serif; color: var(--white); text-transform: uppercase;
    text-shadow: 0 1px 3px rgba(0,0,0,.35);
  }
  .tagline {
    position: absolute; top: 950px; left: 0; width: 995px; text-align: center;
    font: 500 27px "Oswald", sans-serif; color: var(--cream); letter-spacing: 1px;
  }
  .info {
    position: absolute; left: 0; width: 995px; text-align: center;
    font: 700 21px "Arimo", sans-serif; color: var(--info);
  }
  .info-tickets { top: 1025px; }
  .info-venue { top: 1085px; }
  .info-venue svg { vertical-align: -2px; margin-right: 14px; }
</style>
</head>
<body>
<main class="poster">
  <div class="poster-art" role="img" aria-label="Textured illustration of a sunburst sky over layered blue Colorado mountains and pine trees"></div>

  <svg class="poster-frame" width="995" height="1200" viewBox="0 0 995 1200" aria-hidden="true">
    <rect x="24" y="24" width="947" height="1152" fill="none" stroke="var(--frame)" stroke-width="3" stroke-dasharray="1 7" stroke-linecap="round"/>
    <path d="M70,42 H925 A28,28 0 0 0 953,70 V1130 A28,28 0 0 0 925,1158 H70 A28,28 0 0 0 42,1130 V70 A28,28 0 0 0 70,42 Z" fill="none" stroke="var(--frame)" stroke-width="3"/>
  </svg>

  <svg class="ribbon" width="995" height="600" viewBox="0 0 995 600" aria-hidden="true">
    <path d="M292,88 L318,112 L296,140 L340,150 L340,102 Z" fill="var(--ribbon-dark)"/>
    <path d="M703,100 L678,124 L698,152 L655,160 L655,112 Z" fill="var(--ribbon-dark)"/>
    <path d="M320,86 Q500,72 680,100 L676,160 Q500,132 324,150 Z" fill="var(--ribbon)"/>
    <path d="M140,442 L200,497 L150,552 L230,557 L235,462 Z" fill="var(--ribbon-dark)"/>
    <path d="M860,482 L800,532 L845,592 L765,582 L765,492 Z" fill="var(--ribbon-dark)"/>
    <path d="M190,440 Q500,412 820,482 L810,582 Q500,512 200,557 Z" fill="var(--ribbon)"/>
  </svg>

  <p class="edition">6TH ANNUAL</p>
  <h1 class="festival-name"><span class="lead">Pass the</span><span class="main">Echo</span></h1>
  <p class="dates">May 11th - 13th, 2018</p>

  <ul class="lineup">
    <li>Miles Harlow Band • All Hands Orchestra</li>
    <li>Loop Theory • The Pine Cones • J-Roe &amp; The Summit</li>
    <li>Kestrel • Nucleotide • Alpenglow Ensemble</li>
    <li>Sundyed Holofonics • Spyglass • Vivid Optic</li>
    <li>Rail Switch • Orbits</li>
  </ul>

  <svg class="ribbon" width="995" height="1200" viewBox="0 0 995 1200" aria-hidden="true">
    <path d="M235,942 H760 L748,968 L760,994 H235 L247,968 Z" fill="var(--ribbon-dark)"/>
  </svg>
  <p class="tagline">HIGH PLAINS SOUND GATHERING</p>

  <p class="info info-tickets">Tickets &amp; More Info @ www.passtheechofest.com</p>
  <p class="info info-venue">
    <svg width="14" height="20" viewBox="0 0 14 20" aria-hidden="true"><path d="M7,0 C3,0 0,3 0,7 C0,12 7,20 7,20 C7,20 14,12 14,7 C14,3 11,0 7,0 Z M7,10 A3,3 0 1 1 7,4 A3,3 0 1 1 7,10 Z" fill="var(--info)"/></svg>Wren Street Yard - 418 W. 52nd Ave Denver, CO 80221
  </p>
</main>
</body>
</html>
```